Vintage "Greetings from Door County" Design for Wall

I are looking to recreate the vintage "Greetings from" postcard graphic from the 1940-50s. The main focus will be the saying "Greetings from Door County". Door County is a resort area in Wisconsin and we will use this graphic as a backdrop for tourist's instagram pictures. The letters of "Door County" will include things that the area is known for such as swimming, fishing, beaches, boating, biking, camping, cherry orchards, sunsets on the water etc. I have attached an actual postcard from the 50s for Door County to help you visualize the project (Picture 1). I have also attached landmarks and iconic features of Door County to include in the letters (Pictures 2-10). I want it to be more whimsical in nature with drawings to depict these landmarks as opposed to actual realistic pictures (Example 1 & 2). Please ask any questions to help clarify the project. Thanks and good luck!
Target Market(s)
Tourists
Industry/Entity Type
Retail
Colors
Designer to choose colors to be used in the design.
Look and feel

```html
<!DOCTYPE html>
<html lang="en">
<head>
<meta charset="utf-8">
<title>Greetings from Door County, Wisconsin</title>
<link rel="stylesheet" href="https://fonts.googleapis.com/css2?family=Bowlby+One&family=Yellowtail&display=swap">
<style>
  :root {
    --card-cream: #eee8d3;
    --card-edge: #d9d1b8;
    --sky-gold: #f7d22c;
    --sky-amber: #f6a51f;
    --sky-orange: #f27a2a;
    --sky-pink: #ec3f7a;
    --sky-magenta: #b8318c;
    --sea-light: #7fe0ea;
    --sea-deep: #3cc4d6;
    --sun: #ffd21f;
    --ink-navy: #2b2a8c;
    --shade-red: #d3283c;
    --outline-white: #ffffff;
    --fill-bluff: #6f8f4a;
    --fill-ferry: #e8eef4;
    --fill-barn: #b5574a;
    --fill-autumn: #e0772a;
    --fill-theatre: #8fae86;
    --fill-cherry: #c3142a;
    --fill-fire: #f28c1c;
    --fill-shore: #8d8673;
    --fill-tower: #a9cdea;
    --fill-lighthouse: #4f8d5a;
  }
  * { margin: 0; padding: 0; box-sizing: border-box; }
  html, body { width: 1200px; height: 857px; overflow: hidden; background: var(--card-cream); }
  .postcard {
    position: relative;
    width: 1200px; height: 857px;
    background: var(--card-cream);
    border-radius: 22px;
    box-shadow: inset 0 0 0 3px var(--card-edge);
  }
  .postcard__scene {
    position: absolute;
    left: 48px; top: 44px;
    width: 1104px; height: 764px;
    border-radius: 14px;
    overflow: hidden;
  }
  .postcard__art { position: absolute; inset: 0; }
  .headline { position: absolute; left: 0; top: 0; width: 1200px; height: 857px; }
  .block-letters { font-family: "Bowlby One", "Arial Black", sans-serif; }
  .block-letters__shade { fill: var(--shade-red); stroke: var(--ink-navy); stroke-width: 4; paint-order: stroke; stroke-linejoin: round; }
  .block-letters__face { stroke: var(--outline-white); stroke-width: 5; paint-order: stroke; stroke-linejoin: round; }
  .block-letters__rim { fill: none; stroke: var(--ink-navy); stroke-width: 11; stroke-linejoin: round; }
  .script { font-family: "Yellowtail", cursive; fill: var(--ink-navy); stroke: var(--outline-white); stroke-width: 4; paint-order: stroke; stroke-linejoin: round; }
</style>
</head>
<body>
<div class="postcard">
  <div class="postcard__scene">
    <svg class="postcard__art" viewBox="0 0 1104 764" role="img" aria-label="Sunset beach illustration with palm tree silhouettes, a beach chair under an umbrella and a distant island with a pavilion">
      <defs>
        <linearGradient id="sky" x1="0" y1="0" x2="0" y2="1">
          <stop offset="0" stop-color="var(--sky-gold)"/>
          <stop offset="0.4" stop-color="var(--sky-amber)"/>
          <stop offset="0.65" stop-color="var(--sky-orange)"/>
          <stop offset="0.82" stop-color="var(--sky-pink)"/>
          <stop offset="1" stop-color="var(--sky-magenta)"/>
        </linearGradient>
        <linearGradient id="sea" x1="0" y1="0" x2="0" y2="1">
          <stop offset="0" stop-color="var(--sea-deep)"/>
          <stop offset="1" stop-color="var(--sea-light)"/>
        </linearGradient>
      </defs>
      <rect width="1104" height="645" fill="url(#sky)"/>
      <circle cx="712" cy="650" r="90" fill="var(--sun)" opacity="0.95"/>
      <rect y="644" width="1104" height="120" fill="url(#sea)"/>
    </svg>
  </div>

  <svg class="headline" viewBox="0 0 1200 857">
    <g class="block-letters" font-size="236">
      <text class="block-letters__shade" x="250" y="402" textLength="730" lengthAdjust="spacingAndGlyphs">DOOR</text>
      <text class="block-letters__rim" x="240" y="392" textLength="730" lengthAdjust="spacingAndGlyphs">DOOR</text>
      <text class="block-letters__face" x="240" y="392" textLength="730" lengthAdjust="spacingAndGlyphs"><tspan fill="var(--fill-bluff)">D</tspan><tspan fill="var(--fill-ferry)">O</tspan><tspan fill="var(--fill-barn)">O</tspan><tspan fill="var(--fill-autumn)">R</tspan></text>
    </g>
    <g class="block-letters" font-size="232" transform="rotate(3 620 560)">
      <text class="block-letters__shade" x="122" y="652" textLength="1000" lengthAdjust="spacingAndGlyphs">COUNTY</text>
      <text class="block-letters__rim" x="112" y="642" textLength="1000" lengthAdjust="spacingAndGlyphs">COUNTY</text>
      <text class="block-letters__face" x="112" y="642" textLength="1000" lengthAdjust="spacingAndGlyphs"><tspan fill="var(--fill-theatre)">C</tspan><tspan fill="var(--fill-cherry)">O</tspan><tspan fill="var(--fill-fire)">U</tspan><tspan fill="var(--fill-shore)">N</tspan><tspan fill="var(--fill-tower)">T</tspan><tspan fill="var(--fill-lighthouse)">Y</tspan></text>
    </g>
    <text class="script" x="62" y="350" font-size="82" transform="rotate(-12 62 350)">Greetings</text>
    <text class="script" x="108" y="450" font-size="82" transform="rotate(-12 108 450)">from</text>
    <text class="script" x="508" y="720" font-size="72">Wisconsin</text>
  </svg>
</div>
</body>
</html>
```